Jewelry & Bead Show company needs a compelling flyer design

We're a jewelry & bead show organizer, producing over 40 shows a year in different U.S. cities. We need a flyer design that excites customers (who are mainly women), and makes them want to attend the shows. Our show exhibitors are gem/jewelry/bead dealers from around the world, selling merchandise ranging from $1 to thousands of dollars a piece. Flyer dimensions are 6.5" H x 8.5" W, double-sided. The mailing label must be 3" H x 4.5" W. Flyer template is attached.

Target Market(s)

Women 18+

Industry/Entity Type

It Company

Requirements
Must have
• Here are messages to be included:
• -Lustra Fest (big & bold)
• -Why wait, buy on site with confidence at Lustra Fest! Connect face to face with the direct source and Artisans for latest fashion & the best deals!
• -Your FREE pass enclosed
• -Show city, date & facility
• On the back side, there must be an area for show calendar (dates & cities), enough space for 10 shows
Nice to have
• An image of crowd/attendees shopping at a jewelry show.
Should not have
• Diamond images

```html
<!DOCTYPE html>
<html lang="en">
<head>
<meta charset="utf-8">
<title>Lustra Fest Flyer</title>
<link rel="stylesheet" href="https://fonts.googleapis.com/css2?family=Oswald:wght@500&family=Open+Sans:wght@400;600;700&display=swap">
<style>
  :root {
    --page: #ffffff;
    --paper: #dcdde8;
    --paper-deep: #c9cad8;
    --rust: #c1502e;
    --ink: #3a3a48;
    --muted: #6a6a7a;
    --white: #ffffff;
    --stripe: #b7b8c6;
    --rule: #e3e3ea;
  }
  * { box-sizing: border-box; margin: 0; padding: 0; }
  html, body { width: 900px; height: 1200px; overflow: hidden; background: var(--page); }
  body { font-family: "Open Sans", Arial, sans-serif; color: var(--ink); }
  .canvas { position: relative; width: 900px; height: 1200px; }
  .flyer {
    position: absolute; left: 84px; width: 732px; height: 560px;
    background: linear-gradient(180deg, var(--paper) 0%, var(--paper-deep) 100%);
    overflow: hidden;
  }
  .flyer--front { top: 20px; }
  .flyer--back { top: 620px; }

  .base-band { position: absolute; left: 0; right: 0; bottom: 0; height: 64px; background: var(--stripe); }
  .base-band::before { content: ""; position: absolute; left: 0; right: 0; top: 0; height: 22px; background: var(--rust); }

  /* front */
  .photo-cluster { position: absolute; left: 18px; top: 16px; width: 270px; height: 300px; }
  .brand { position: absolute; right: 28px; top: 24px; display: flex; align-items: center; gap: 8px; }
  .brand__mark { width: 16px; height: 16px; background: var(--rust); }
  .brand__name { font-family: "Oswald", Arial, sans-serif; font-weight: 500; font-size: 24px; color: var(--rust); text-transform: uppercase; }
  .title-banner {
    position: absolute; left: 300px; right: 0; top: 120px; height: 56px;
    background: var(--rust); padding-left: 20px; display: flex; align-items: center;
  }
  .title-banner h1 { font-family: "Oswald", Arial, sans-serif; font-weight: 500; font-size: 36px; color: var(--white); letter-spacing: 1px; text-transform: uppercase; }
  .intro { position: absolute; left: 300px; right: 30px; top: 188px; font-size: 12px; line-height: 1.5; }
  .intro strong { color: var(--rust); font-weight: 600; }
  .mail-label { position: absolute; left: 300px; top: 272px; width: 340px; height: 190px; background: var(--white); }

  .show-info { position: absolute; left: 24px; top: 330px; width: 252px; }
  .show-info__tagline { font-size: 11px; line-height: 1.5; margin-bottom: 10px; }
  .show-info__pass {
    display: inline-block; background: var(--rust); color: var(--white);
    font-family: "Oswald", Arial, sans-serif; font-weight: 500; font-size: 16px;
    padding: 3px 12px; margin-bottom: 8px; text-transform: uppercase;
  }
  .show-info__details { font-size: 12px; line-height: 1.45; }
  .show-info__details strong { font-weight: 700; }

  /* back */
  .gem-cluster { position: absolute; right: 6px; top: 14px; width: 400px; height: 310px; }
  .calendar {
    position: absolute; left: 0; top: 300px; width: 330px; height: 190px;
    background: var(--white); padding: 12px 16px;
  }
  .calendar__title {
    font-family: "Oswald", Arial, sans-serif; font-weight: 500; font-size: 16px;
    color: var(--rust); text-transform: uppercase; margin-bottom: 6px;
  }
  .calendar__list { list-style: none; display: grid; grid-template-columns: 1fr 1fr; column-gap: 16px; }
  .calendar__list li {
    display: flex; justify-content: space-between; font-size: 11px; line-height: 1;
    padding: 6px 0; border-bottom: 1px solid var(--rule);
  }
  .calendar__list span:first-child { color: var(--muted); }

  .contact { position: absolute; left: 390px; top: 350px; }
  .contact__tab {
    display: inline-block; background: var(--rust); color: var(--white);
    font-family: "Oswald", Arial, sans-serif; font-weight: 500; font-size: 17px; padding: 4px 14px; margin-bottom: 12px;
  }
  .contact__list { list-style: none; font-size: 13px; }
  .contact__list li { display: flex; align-items: center; gap: 10px; margin-bottom: 8px; }
  .contact__list svg { width: 16px; height: 16px; fill: var(--ink); }
</style>
</head>
<body>
<main class="canvas">

  <section class="flyer flyer--front" aria-label="Flyer front">
    <svg class="photo-cluster" viewBox="0 0 270 300" role="img" aria-label="Hexagon photos of shoppers browsing jewelry and bead stands">
      <defs>
        <linearGradient id="photoTone" x1="0" y1="0" x2="1" y2="1">
          <stop offset="0" stop-color="#c89a86"/>
          <stop offset="1" stop-color="#6b5a6e"/>
        </linearGradient>
        <linearGradient id="beadTone" x1="0" y1="0" x2="0" y2="1">
          <stop offset="0" stop-color="#b2452e"/>
          <stop offset="1" stop-color="#3e6b5c"/>
        </linearGradient>
      </defs>
      <polygon points="40,10 110,10 145,70 110,130 40,130 5,70" fill="url(#photoTone)" stroke="#fff" stroke-width="4"/>
      <polygon points="155,10 225,10 260,70 225,130 155,130 120,70" fill="url(#photoTone)" stroke="#fff" stroke-width="4"/>
      <polygon points="97,100 167,100 202,160 167,220 97,220 62,160" fill="url(#beadTone)" stroke="#fff" stroke-width="4"/>
      <polygon points="40,170 110,170 145,230 110,290 40,290 5,230" fill="url(#photoTone)" stroke="#fff" stroke-width="4"/>
    </svg>

    <div class="brand">
      <span class="brand__mark"></span>
      <span class="brand__name">Lustra Fest</span>
    </div>

    <div class="title-banner"><h1>Lustra Fest</h1></div>

    <p class="intro">We're a jewelry &amp; bead show organizer, producing over <strong>40 shows</strong> a year in different <strong>U.S.</strong> cities. Our show exhibitors are <strong>gem/jewelry/bead</strong> dealers from around the world, selling merchandise ranging from $1 to thousands of dollars a piece.</p>

    <div class="show-info">
      <p class="show-info__tagline">Why wait, buy on site with confidence at Lustra Fest! Connect face to face with the direct source and Artisans for latest fashion &amp; the best deals!</p>
      <span class="show-info__pass">Your FREE pass enclosed</span>
      <p class="show-info__details"><strong>Denver, CO</strong> &middot; May 16–18<br>Riverside Expo Hall</p>
    </div>

    <div class="mail-label"></div>
    <div class="base-band"></div>
  </section>

  <section class="flyer flyer--back" aria-label="Flyer back">
    <svg class="gem-cluster" viewBox="0 0 400 310" role="img" aria-label="Scattered colourful gemstones and beads">
      <defs>
        <radialGradient id="gemTone" cx="0.55" cy="0.45" r="0.5">
          <stop offset="0" stop-color="#7a5aa0"/>
          <stop offset="0.4" stop-color="#3f8fb0"/>
          <stop offset="0.7" stop-color="#d0743c" stop-opacity="0.85"/>
          <stop offset="1" stop-color="#dcdde8" stop-opacity="0"/>
        </radialGradient>
      </defs>
      <ellipse cx="200" cy="155" rx="195" ry="150" fill="url(#gemTone)"/>
    </svg>

    <div class="calendar">
      <h2 class="calendar__title">Show Calendar</h2>
      <ul class="calendar__list">
        <li><span>Jan 10–12</span><span>Tucson, AZ</span></li>
        <li><span>Jun 06–08</span><span>Dallas, TX</span></li>
        <li><span>Feb 14–16</span><span>San Diego, CA</span></li>
        <li><span>Jul 11–13</span><span>Chicago, IL</span></li>
        <li><span>Mar 07–09</span><span>Phoenix, AZ</span></li>
        <li><span>Aug 15–17</span><span>Atlanta, GA</span></li>
        <li><span>Apr 11–13</span><span>Portland, OR</span></li>
        <li><span>Sep 19–21</span><span>Boston, MA</span></li>
        <li><span>May 16–18</span><span>Denver, CO</span></li>
        <li><span>Oct 24–26</span><span>Tampa, FL</span></li>
      </ul>
    </div>

    <div class="contact">
      <span class="contact__tab">Contact Us</span>
      <ul class="contact__list">
        <li><svg viewBox="0 0 24 24" aria-hidden="true"><path d="M6.6 10.8a15 15 0 0 0 6.6 6.6l2.2-2.2a1 1 0 0 1 1-.25 11.4 11.4 0 0 0 3.6.6 1 1 0 0 1 1 1V20a1 1 0 0 1-1 1A17 17 0 0 1 3 4a1 1 0 0 1 1-1h3.5a1 1 0 0 1 1 1c0 1.25.2 2.450.6 3.6a1 1 0 0 1-.25 1z"/></svg>0100-555-0199</li>
        <li><svg viewBox="0 0 24 24" aria-hidden="true"><path d="M12 2a10 10 0 1 0 0 20 10 10 0 0 0 0-20zm0 2c1 0 2.3 2 2.8 5H9.2C9.7 6 11 4 12 4zM4.3 11h3.9a20 20 0 0 0 0 2H4.3a8 8 0 0 1 0-2zm1 4h3.2c.3 1.6.8 3 1.5 4.1A8 8 0 0 1 5.3 15zm0-6a8 8 0 0 1 4.7-4.1A13 13 0 0 0 8.5 9zM12 20c-1 0-2.3-2-2.8-5h5.6c-.5 3-1.8 5-2.8 5zm3.1-7H8.9a18 18 0 0 1 0-2h6.2a18 18 0 0 1 0 2zm-1.1 6.1c.7-1.1 1.2-2.5 1.5-4.1h3.2a8 8 0 0 1-4.7 4.1zM15.8 13a20 20 0 0 0 0-2h3.9a8 8 0 0 1 0 2zm-.3-4A13 13 0 0 0 14 4.9 8 8 0 0 1 18.7 9z"/></svg>www.lustrafest-shows.com</li>
        <li><svg viewBox="0 0 24 24" aria-hidden="true"><path d="M3 5h18a1 1 0 0 1 1 1v12a1 1 0 0 1-1 1H3a1 1 0 0 1-1-1V6a1 1 0 0 1 1-1zm1 2.2V17h16V7.2l-8 5.3z M5 7l7 4.6L19 7z"/></svg>info@lustrafest-shows.com</li>
      </ul>
    </div>

    <div class="base-band"></div>
  </section>

</main>
</body>
</html>
```